Design for Cat & Dog Sites

Hi,

I need a standard WP theme and logo with the following requirements:
- the Logo needs to be wordbased, Only font. Color should somehow fit to pets.
- there should be a picture of an animal in the header/background, which needs to be interchangeable in order to make different sites for different sorts of animals
- the theme will be used for sites about pets in general, especially cats and dogs

Here is an example how it can be done for different countries:
http://www.velmorast.org/
http://www.quorvelin.net/
http://www.tesmarund.net/

There should be a sitebar, which we can link to all categories

Only a design is needed, we will do the coding + implementation ourselves.

There is no Icon needed, only a font that can be changed for each site

Important: the design must be interchangeable so standard elements must fit to a pet theme in general

Target Market(s)

People that want information about cats, dogs and the certain races they have.

Industry/Entity Type

Pet

Requirements
Must have
• interchangeable
- logo as a font
- header / background
- sitebar, which can list all categories similar to velmorast.org

```html
<!DOCTYPE html>
<html lang="en">
<head>
<meta charset="utf-8">
<title>Pawlora</title>
<link rel="stylesheet" href="https://fonts.googleapis.com/css2?family=Arimo:wght@400;700&display=swap">
<style>
:root{
  --teal:#3fb9c9;
  --teal-dark:#2aa3b5;
  --teal-light:#5fd0dc;
  --text:#333;
  --muted:#666;
  --panel:#f1f1f1;
  --footer:#2e2e2e;
  --footer-bottom:#262626;
  --footer-text:#ddd;
  --link-blue:#3f5f9a;
}
*{box-sizing:border-box;margin:0;padding:0}
html,body{width:862px;height:1200px;overflow:hidden}
body{font-family:"Arimo",Arial,sans-serif;color:var(--text);background:#fff;position:relative}
.abs{position:absolute}

.hero{left:0;top:0;width:862px;height:444px;background:linear-gradient(100deg,#dfe4ea 0%,#c9b08a 18%,#b98a4c 30%,#d8dde3 45%,#3e4655 60%,#48505c 80%,#e6e8ec 100%)}
.topbar{left:64px;top:22px;width:734px;height:59px;background:linear-gradient(#55cdd9,#35b0c2);border-radius:3px;box-shadow:0 2px 3px rgba(0,0,0,.35)}
.logo{left:20px;top:10px;font-size:34px;font-weight:700;color:#fff}
.nav{right:0;top:16px;display:flex;list-style:none}
.nav li{font-size:11px;font-weight:700;color:#fff;padding:0 14px;height:26px;line-height:26px;border-left:1px solid rgba(255,255,255,.25)}
.nav li:first-child{border-left:none}
.nav li.active{background:#2a2a2a;border-radius:3px;padding:0 9px;margin-right:8px}

.welcome{left:477px;top:121px;width:306px;height:284px;background:rgba(240,240,240,.88);padding:26px 22px 0 23px}
.welcome h1{font-size:17px;color:var(--teal);margin-bottom:12px}
.welcome p{font-size:10.2px;line-height:18px;text-align:justify;color:#222}
.btn-light{display:inline-block;margin-top:12px;padding:5px 12px;font-size:10px;font-weight:700;color:#555;background:linear-gradient(#fff,#ddd);border-radius:3px;box-shadow:0 1px 2px rgba(0,0,0,.3)}
.dots{left:701px;top:418px;display:flex;gap:11px}
.dots span{width:12px;height:12px;border-radius:50%;background:#333}
.dots span:first-child{background:#eee;border:2px solid #333}

.crumb{left:70px;top:454px;font-size:9px;color:#555}
.crumb b{font-weight:400;color:#000}

.main{left:64px;top:474px;width:734px;height:512px;background:var(--panel)}
.h2{font-size:16px;font-weight:700;color:var(--teal)}
.body-text{font-size:9px;line-height:16.5px;color:#444;text-align:justify}
.photo-frame{background:#fff;padding:3px;box-shadow:0 1px 3px rgba(0,0,0,.25)}
.photo{width:100%;height:100%}
.btn-dark{display:inline-block;padding:6px 9px;font-size:10px;color:#fff;background:linear-gradient(#555,#2e2e2e);border-radius:3px}
.divider{left:72px;top:724px;width:723px;height:1px;background:#ddd}

.side-head{width:213px;height:30px;background:linear-gradient(#4cc4d2,#34aebf);border:1px solid #2b9fb0;color:#111;font-size:12px;line-height:28px;padding-left:15px}
.side-head i{position:absolute;right:12px;top:8px;width:12px;height:12px;border-radius:50%;background:#2489a0}
.side-head i::after{content:"";position:absolute;left:4px;top:3px;border-left:4px solid #fff;border-top:3px solid transparent;border-bottom:3px solid transparent}
.news{width:213px;background:#fff;padding:12px 14px 0 14px;list-style:none}
.news li{position:relative;padding-left:14px;margin-bottom:17px;font-size:8.8px;line-height:12.5px;color:#333}
.news li::before{content:"";position:absolute;left:2px;top:3px;border-left:5px solid #555;border-top:4px solid transparent;border-bottom:4px solid transparent}
.news .date{display:block;color:var(--teal-dark);margin-top:4px}
.testi{width:213px;padding:20px 16px 0 16px;background:#f4f4f4;height:187px}
.testi p{font-size:11.5px;line-height:18px;color:#555}
.testi .q{font-size:20px;color:#bbb;font-weight:700;line-height:0}
.testi .who{display:block;margin-top:10px;font-size:10px;color:var(--link-blue)}

.card{width:150px;height:136px;background:#fff;box-shadow:0 1px 3px rgba(0,0,0,.18);padding:10px 6px 0 6px}
.card h3{font-size:12px;font-weight:400;color:var(--teal-dark);margin:0 0 7px 4px}
.card .photo-frame{height:96px}

.footer{left:0;top:986px;width:862px;height:174px;background:var(--footer)}
.foot-bottom{left:0;top:1160px;width:862px;height:40px;background:var(--footer-bottom);text-align:center;font-size:9px;line-height:40px;color:#aaa}
.fh{font-size:12px;color:var(--teal-light);font-weight:400}
.flist{list-style:none;font-size:8.8px;color:var(--footer-text)}
.flist li{margin-top:9px}
.flist li::before{content:"• "}
.field{width:164px;height:20px;background:#fff;border:1px solid #ccc;font-size:8px;padding-left:11px;line-height:18px;color:#333}
.submit{background:linear-gradient(#55cdd9,#2fa9bb);color:#fff;font-size:10px;font-weight:700;padding:4px 7px}
.contact{list-style:none;font-size:8.8px;color:var(--footer-text);line-height:15px}
.contact li{margin-top:7px;padding-left:9px;position:relative}
.contact li::before{content:"•";position:absolute;left:0}
.social{list-style:none;font-size:8.8px;color:var(--footer-text)}
.social li{display:flex;align-items:center;height:20px;margin-bottom:10px}
.social .sq{width:19px;height:19px;border-radius:2px;margin-right:17px}
.social b{font-weight:400;color:var(--teal-light);font-size:10.5px;margin-left:5px}
</style>
</head>
<body>

<div class="abs hero" role="img" aria-label="Golden retriever standing in a bright living room beside a dark sofa"></div>

<header class="abs topbar">
  <div class="abs logo">Pawlora</div>
  <ul class="abs nav">
    <li class="active">Home</li><li>About</li><li>Services</li><li>Products</li><li>Contact</li>
  </ul>
</header>

<section class="abs welcome">
  <h1>Welcome to Pawlora</h1>
  <p>Mauris ut erat ligula. Duis euismod nisi vitae diam tempus eget tempus nibh consectetur. Etiam ac est ac nisi imperdiet vehicula quis nec purus. Maecenas nec lacus sed enim commodo tincidunt id nec ante. Nulla nunc dui, suscipit nec accumsan non, malesuada tincidunt purus. Integer lobortis accumsan lacus sed venenatis. Phasellus vel est augue, adipiscing mollis velit. Duis lobortis vehicula arcu, vitae venenatis mauris pulvinar gravida. Lorem ipsum dolor sit amet, consectetur adipiscing elit.</p>
  <span class="btn-light">View more</span>
</section>
<div class="abs dots"><span></span><span></span><span></span><span></span></div>

<nav class="abs crumb"><b>Home</b> &nbsp;&gt;&gt;&nbsp; Welcome</nav>

<main class="abs main"></main>

<section class="abs" style="left:73px;top:490px;width:490px">
  <h2 class="h2">About Pawlora</h2>
</section>
<p class="abs body-text" style="left:73px;top:520px;width:300px">Mauris ut erat ligula. Duis euismod nisi vitae diam tempus eget tempus nibh consectetur. Etiam ac est ac nisi imperdiet vehicula quis nec purus. Maecenas nec lacus sed enim commodo tincidunt id nec ante. Nulla nunc dui, suscipit nec accumsan non, malesuada tincidunt purus. Integer lobortis accumsan lacus sed venenatis. Phasellus vel est augue, adipiscing mollis velit. Duis lobortis vehicula arcu, vitae venenatis.</p>
<div class="abs photo-frame" style="left:388px;top:524px;width:174px;height:91px">
  <div class="photo" role="img" aria-label="Dog and kitten lying together on a white background" style="background:linear-gradient(90deg,#f4f1ec,#c98e4e 45%,#e7dccb 75%,#f6f4f0)"></div>
</div>
<p class="abs body-text" style="left:73px;top:630px;width:490px">Curabitur nec eros nulla. Nam vestibulum aliquam metus, nec rutrum dui ornare ut. Sed id mattis lectus. Class aptent taciti sociosqu ad litora torquent per conubia nostra, per inceptos himenaeos. Fusce vel tellus tellus.</p>
<span class="abs btn-dark" style="left:73px;top:674px">View more</span>

<div class="abs divider"></div>

<h2 class="abs h2" style="left:73px;top:743px">Pawlora Services</h2>
<p class="abs body-text" style="left:73px;top:772px;width:490px">Sed quis magna nunc, sed imperdiet tellus. In laoreet condimentum egestas. Lorem ipsum dolor sit amet, consectetur adipiscing elit. Integer mattis orci sed erat gravida quis vulputate sapien adipiscing. Nunc ac dapibus urna. Aenean ornare mauris eu ante vulputate tincidunt. Mauris molestie viverra ipsum nec feugiat.</p>

<article class="abs card" style="left:72px;top:833px">
  <h3>Health Advices</h3>
  <div class="photo-frame"><div class="photo" role="img" aria-label="Small terrier sitting in snow under a blue sky" style="background:linear-gradient(#a9c4e4,#dfe8f2 60%,#c8b8a0)"></div></div>
</article>
<article class="abs card" style="left:240px;top:833px">
  <h3>Pet Poducts</h3>
  <div class="photo-frame"><div class="photo" role="img" aria-label="Red leash and brown leather dog collar" style="background:linear-gradient(135deg,#fff,#f2d2c8 40%,#c98a45 65%,#fff)"></div></div>
</article>
<article class="abs card" style="left:409px;top:833px">
  <h3>Food Products</h3>
  <div class="photo-frame"><div class="photo" role="img" aria-label="Cat and dog eating from metal bowls" style="background:linear-gradient(90deg,#6b5848,#b78459 55%,#8a5a35 80%,#c9c9c9)"></div></div>
</article>

<aside class="abs" style="left:578px;top:494px">
  <div class="side-head" style="position:relative">Latest News<i></i></div>
  <ul class="news" style="height:186px">
    <li>Nulla nunc dui, suscipit nec accumsan non, malesuada tincidunt purus.<span class="date">Feb-20-2013</span></li>
    <li>Nulla nunc dui, suscipit nec accumsan non, malesuada tincidunt purus.<span class="date">Feb-20-2013</span></li>
    <li>Nulla nunc dui, suscipit nec accumsan non, malesuada tincidunt purus.<span class="date">Feb-20-2013</span></li>
  </ul>
</aside>

<aside class="abs" style="left:578px;top:747px">
  <div class="side-head" style="position:relative">Testimonials<i></i></div>
  <div class="testi">
    <p><span class="q">&ldquo;</span> Caecenas est dolor, consectetur et pretium vel, adipiscing in tortor. Aenean nec mauris in orci venenatis fermentum. Vestibulum in blandit nibh. Maecenas a ligula dui. Donec fermentum euismod sapien at feugiat. Aliquam erat volutpat. <span class="q">&rdquo;</span></p>
    <span class="who">Client Name, City</span>
  </div>
</aside>

<footer class="abs footer">
  <div class="abs" style="left:64px;top:16px">
    <h4 class="fh">Quick Links</h4>
    <ul class="flist" style="margin-top:4px;line-height:12px">
      <li>Pellentesque laoreet</li><li>Suspendisse</li><li>Pellentesque habitant</li><li>Morbi nuncquam</li><li>Etiamarcu ante</li><li>Aenean eu</li>
    </ul>
  </div>
  <div class="abs" style="left:244px;top:16px">
    <h4 class="fh">Email Signup</h4>
    <div class="field" style="margin-top:14px">Name</div>
    <div class="field" style="margin-top:11px">Email ID</div>
    <div style="text-align:right;width:164px;margin-top:10px"><span class="submit">SUBMIT</span></div>
  </div>
  <div class="abs" style="left:476px;top:16px">
    <h4 class="fh">Quick contact</h4>
    <ul class="contact" style="margin-top:3px">
      <li>Pawlora<br>18, Linden Hollow Lane<br>Brookvale, BV204</li>
      <li>Call Us : 555 310 4821</li>
      <li>Fax : 555 310 4877</li>
      <li>E-mail : info@pawlora.com</li>
    </ul>
  </div>
  <div class="abs" style="left:649px;top:16px">
    <h4 class="fh">Connect with us</h4>
    <ul class="social" style="margin-top:12px">
      <li><span class="sq" style="background:#5b7bb5"></span>Join with us on<b>Friendwall</b></li>
      <li><span class="sq" style="background:#5ec3e6"></span>Follow us on<b>Chirpline</b></li>
      <li><span class="sq" style="background:#2a76b4"></span>Share on<b>Linkfold</b></li>
      <li><span class="sq" style="background:#d64a3c"></span>Watch on<b>Viewcast</b></li>
    </ul>
  </div>
</footer>
<div class="abs foot-bottom">Copyright &copy; 2013 &nbsp; www.pawlora.com &nbsp; All rights reserved.</div>

</body>
</html>
```